Personal Training Business at home (Fern Wellness & Health)

My business name will be Fern Wellness & Health and will be training people with special needs (Asthma, Diabetes, Obesity, Rehab, Sports Performance) for all ages. It will be set indoor and outdoor for all types of weather conditions. I,m also doing Pilates group classes as well in a Japanese garden setting.I will be working alone so the groups will be small and the client has a high quality of service. I just need something very basic to start with then as the business expands I can edit it to it,s growth.

Target Market(s)

Target special population persons with dysfunctions injuries, metabolic/cardio-respiratory conditions, sports performance and more also healthy food choices.

Industry/Entity Type

Business

Number of Pages Required

3 page

Font styles to use
Serif

Colors
f78f20
ffffff
474747
cbcbcb
abd036

Requirements
Must have
• The website must have accessibility for change, to be able to link on other networks like my own YouTube videos. A basic lay out so I can fill in the pages and ad more as I expand the business. The logo to have the A for Arch to be an image of a man shaped as the letter A with his arms extended out/up. Private Facility and must ring for appointment to enter premises.
Nice to have
• The Image I want to have in my studio is for people to be serious about training & health choices. I want them to be able to train in a comfortable environment and free of air conditioned concrete rooms with machines. My home is converted to a Organic feature and outdoor/indoor training facility that my clients & I can share the natural freedom of training in the elements. My client have special needs and need extra care, they are people with injuries, metabolic/cardio-respiratory condition, asthmatics & more they need to be screened and tested for the condition that they suffer from and together with there allied professional we work together to treat them with the up most care for maximum results. This is what I want to target I long term client with real Goals on there mind and not some pipe dream.
Should not have
• Not to be portray as a Gym with machines and clients that only care about image.

```html
<!DOCTYPE html>
<html lang="en">
<head>
<meta charset="utf-8">
<title>Fern Wellness &amp; Health</title>
<link href="https://fonts.googleapis.com/css2?family=Lora:wght@400;500;700&display=swap" rel="stylesheet">
<style>
:root{
  --page:#f5f5f3;
  --white:#ffffff;
  --orange:#f78f20;
  --green:#abd036;
  --ink:#474747;
  --muted:#858585;
  --line:#cbcbcb;
}
*{margin:0;padding:0;box-sizing:border-box}
html,body{width:1200px;height:2400px;overflow:hidden}
body{background:var(--page);font-family:"Lora",serif;color:var(--ink);position:relative}
.abs{position:absolute}

/* header */
.brand{left:200px;top:56px;font-size:27px;font-weight:500;color:var(--orange);white-space:nowrap}
.contact-dot{width:38px;height:38px;border-radius:50%;background:var(--green);display:flex;align-items:center;justify-content:center}
.phone-dot{left:516px;top:50px}
.pin-dot{left:758px;top:50px}
.call-label{left:574px;top:46px;font-size:12px;color:var(--muted)}
.call-number{left:574px;top:64px;font-size:20px;color:var(--ink);letter-spacing:1px}
.address{left:814px;top:52px;font-size:13px;line-height:18px;color:var(--ink)}
.main-nav{right:174px;top:132px;display:flex;gap:22px;font-size:13px;color:var(--muted)}

/* services */
.services{left:172px;top:180px;width:854px;height:356px;background:var(--white);box-shadow:0 6px 14px rgba(0,0,0,.10)}
.service{position:absolute;display:flex;gap:24px;align-items:center}
.service-icon{width:92px;height:92px;border-radius:50%;border:2px solid var(--line);display:flex;align-items:center;justify-content:center;flex:none}
.service-mark{width:36px;height:36px;border-radius:50%;background:var(--orange)}
.service h3{font-size:28px;font-weight:400;color:var(--orange);margin-bottom:8px;white-space:nowrap}
.service p{font-size:11px;line-height:18px;color:var(--muted);width:240px}

/* expect */
.section-title{left:0;width:1200px;text-align:center;font-size:26px;font-weight:500;color:var(--ink)}
.expect-art{left:172px;width:144px;height:150px;border-radius:60px 60px 20px 20px;background:var(--orange)}
.expect-art.round{border-radius:50%;width:124px;height:124px;left:188px}
.expect-title{left:370px;font-size:25px;font-weight:500;color:var(--orange)}
.expect-text{left:370px;width:632px;font-size:13px;line-height:17px;color:var(--ink)}
.see-more{left:532px;top:1354px;width:190px;height:52px;border-radius:4px;background:var(--green);color:var(--ink);font-size:15px;font-weight:500;display:flex;align-items:center;justify-content:center}

/* reviews */
.reviews{left:172px;top:1484px;width:854px;height:298px;background:var(--white);box-shadow:0 6px 14px rgba(0,0,0,.10)}
.review-badge{left:206px;top:1446px;width:74px;height:74px;border-radius:50%;background:var(--orange);border:4px solid var(--white);display:flex;align-items:center;justify-content:center}
.reviews-title{left:292px;top:1504px;font-size:16px;font-weight:700;color:var(--orange)}
.reviews-all{left:930px;top:1502px;font-size:12px;color:var(--muted)}
.review{left:208px;width:800px}
.review-meta{font-size:10px;color:var(--ink)}
.review-meta .stars{color:var(--orange);letter-spacing:1px;margin-right:10px;font-size:11px}
.review-meta b{font-weight:700}
.review p{font-size:10.5px;line-height:17px;margin-top:8px;color:var(--ink)}

/* tweets */
.say-dot{left:474px;top:1862px;width:30px;height:30px;border-radius:50%;background:var(--green)}
.say-title{left:528px;top:1856px;font-size:29px;font-weight:400;color:var(--ink)}
.tweet-band{left:0;top:1960px;width:1200px;height:236px;background:var(--white)}
.tweet{position:absolute;top:2004px;width:366px;height:152px;border:1px solid var(--line);border-radius:4px;background:var(--white);padding:14px 16px;font-size:12px;line-height:17px}
.tweet.faded{opacity:.55}
.tweet-head{display:flex;align-items:center;gap:10px;margin-bottom:8px}
.avatar{width:26px;height:26px;border-radius:3px;background:#c9a48a}
.tweet-name{font-weight:700;font-size:12px;line-height:14px}
.tweet-handle{font-size:10px;color:var(--muted);line-height:12px}
.follow{margin-left:auto;border:1px solid var(--line);border-radius:3px;padding:1px 10px;font-size:10px;color:var(--orange)}
.tweet-text a{color:var(--orange);text-decoration:none}
.tweet-time{font-size:10px;color:var(--muted);margin-top:4px}
.tweet-actions{display:flex;gap:16px;font-size:10px;color:var(--muted);margin-top:6px}
.arrow{top:2066px;color:var(--muted);font-size:22px}

/* footer */
.foot-brand{left:168px;top:2254px;font-size:27px;font-weight:500;color:var(--ink);white-space:nowrap}
.copyright{left:172px;top:2346px;font-size:10px;color:var(--muted)}
.go-top{left:556px;top:2292px;display:flex;align-items:center;gap:8px;font-size:12px;font-weight:700;color:var(--orange)}
.go-top .ring{width:26px;height:26px;border-radius:50%;border:2px solid var(--orange);display:flex;align-items:center;justify-content:center}
.foot-team{left:792px;top:2260px;font-size:18px;font-weight:500;color:var(--ink);display:flex;align-items:center;gap:8px}
.foot-team .mark{width:8px;height:8px;border-radius:50%;background:var(--green)}
.foot-address{left:792px;top:2302px;font-size:14px;line-height:24px;color:var(--muted)}
</style>
</head>
<body>

<header>
  <div class="abs brand">Fern Wellness &amp; Health</div>
  <div class="abs contact-dot phone-dot">
    <svg width="14" height="20" viewBox="0 0 14 20"><rect x="1" y="1" width="12" height="18" rx="2" fill="none" stroke="#fff" stroke-width="2"/><circle cx="7" cy="15.5" r="1.3" fill="#fff"/></svg>
  </div>
  <div class="abs call-label">you can call us</div>
  <div class="abs call-number">1-000-58-21</div>
  <div class="abs contact-dot pin-dot">
    <svg width="14" height="20" viewBox="0 0 14 20"><path d="M7 1C3.7 1 1 3.6 1 7c0 4.5 6 12 6 12s6-7.5 6-12c0-3.4-2.7-6-6-6z" fill="#fff"/><circle cx="7" cy="7" r="2.2" fill="#abd036"/></svg>
  </div>
  <div class="abs address">14 Alder Lane, Kestrel<br>Vale, KV3 9PN</div>
  <nav class="abs main-nav"><span>Home</span><span>Blog</span><span>Recent News</span><span>Meet our team</span><span>Contact</span></nav>
</header>

<section class="abs services">
  <div class="service" style="left:48px;top:42px">
    <div class="service-icon"><div class="service-mark" role="img" aria-label="Pilates pose icon"></div></div>
    <div><h3>Pilates</h3><p>Lorem ipsum dolor sit amet, consectetur adipiscing elit. Pellentesque fringilla orci.</p></div>
  </div>
  <div class="service" style="left:480px;top:42px">
    <div class="service-icon"><div class="service-mark" role="img" aria-label="Massage table icon"></div></div>
    <div><h3>Sports Massage</h3><p>Lorem ipsum dolor sit amet, consectetur adipiscing elit. Pellentesque fringilla orci.</p></div>
  </div>
  <div class="service" style="left:48px;top:220px">
    <div class="service-icon"><div class="service-mark" role="img" aria-label="Yoga pose icon"></div></div>
    <div><h3>Yoga</h3><p>Lorem ipsum dolor sit amet, consectetur adipiscing elit. Pellentesque fringilla orci.</p></div>
  </div>
  <div class="service" style="left:480px;top:220px">
    <div class="service-icon">
      <svg width="34" height="40" viewBox="0 0 34 40"><path d="M8 18v-6a9 9 0 0 1 18 0v6" fill="none" stroke="#f78f20" stroke-width="4"/><rect x="3" y="17" width="28" height="22" rx="3" fill="#f78f20"/><rect x="15" y="24" width="4" height="8" rx="2" fill="#fff"/></svg>
    </div>
    <div><h3>Private Hire</h3><p>Lorem ipsum dolor sit amet, consectetur adipiscing elit. Pellentesque fringilla orci.</p></div>
  </div>
</section>

<h2 class="abs section-title" style="top:604px">What to expect</h2>

<div class="abs expect-art" style="top:700px" role="img" aria-label="Illustration of a person with a heart"></div>
<h3 class="abs expect-title" style="top:696px">Lorem ipsum dolor</h3>
<p class="abs expect-text" style="top:740px">Vestibulum nunc urna, hendrerit molestie convallis nec, blandit non ligula. Nam et purus vitae erat tincidunt convallis nec eu ex. Nulla ut eros risus. Pellentesque varius mi ut imperdiet vestibulum. Phasellus nec felis eros. Nullam velit sapien, mollis et pellentesque in, imperdiet vitae odio. Proin venenatis sem at tellus dictum tincidunt. Interdum et malesuada fames ac ante ipsum primis in faucibus. Morbi et lacinia urna, eget aliquet dolor.</p>

<div class="abs expect-art" style="top:916px;width:130px;left:180px;border-radius:40px" role="img" aria-label="Illustration of a running figure"></div>
<h3 class="abs expect-title" style="top:914px">Lorem ipsum dolor</h3>
<p class="abs expect-text" style="top:958px">Vestibulum nunc urna, hendrerit molestie convallis nec, blandit non ligula. Nam et purus vitae erat tincidunt convallis nec eu ex. Nulla ut eros risus. Pellentesque varius mi ut imperdiet vestibulum. Phasellus nec felis eros. Nullam velit sapien, mollis et pellentesque in, imperdiet vitae odio. Proin venenatis sem at tellus dictum tincidunt. Interdum et malesuada fames ac ante ipsum primis in faucibus. Morbi et lacinia urna, eget aliquet dolor.</p>

<div class="abs expect-art round" style="top:1162px" role="img" aria-label="Illustration of a flowing balance symbol"></div>
<h3 class="abs expect-title" style="top:1144px">Lorem ipsum dolor</h3>
<p class="abs expect-text" style="top:1188px">Vestibulum nunc urna, hendrerit molestie convallis nec, blandit non ligula. Nam et purus vitae erat tincidunt convallis nec eu ex. Nulla ut eros risus. Pellentesque varius mi ut imperdiet vestibulum. Phasellus nec felis eros. Nullam velit sapien, mollis et pellentesque in, imperdiet vitae odio. Proin venenatis sem at tellus dictum tincidunt. Interdum et malesuada fames ac ante ipsum primis in faucibus. Morbi et lacinia urna, eget aliquet dolor.</p>

<div class="abs see-more">SEE MORE</div>

<section class="abs reviews"></section>
<div class="abs review-badge">
  <svg width="34" height="34" viewBox="0 0 24 24"><path d="M12 2l2.9 6.3 6.9.7-5.2 4.6 1.5 6.8L12 16.9 5.9 20.4l1.5-6.8L2.2 9l6.9-.7z" fill="none" stroke="#fff" stroke-width="2" stroke-linejoin="round"/></svg>
</div>
<div class="abs reviews-title">The Reviews Are In</div>
<div class="abs reviews-all">All reviews &nbsp;›</div>

<div class="abs review" style="top:1556px">
  <div class="review-meta"><span class="stars">★★★★★</span>11-27-2015 by <b>Daniel and Rosalind</b> in Millbrook CA</div>
  <p>We want to express our sincere thanks to all of you for all your hard work in making our dream come true.&nbsp; I know a lot of things had to happen behind the scenes and I wanted to thank you for your patience and understanding during this process. ... feel incredibly blessed during this Thanksgiving holiday.</p>
</div>
<div class="abs review" style="top:1624px">
  <div class="review-meta"><span class="stars">★★★★★</span>11-27-2015 by <b>Daniel and Rosalind</b> in Millbrook CA</div>
  <p>We want to express our sincere thanks to all of you for all your hard work in making our dream come true.&nbsp; I know a lot of things had to happen behind the scenes and I wanted to thank you for your patience and understanding during this process. ... feel incredibly blessed during this Thanksgiving holiday.</p>
</div>
<div class="abs review" style="top:1692px">
  <div class="review-meta"><span class="stars">★★★★★</span>11-27-2015 by <b>Daniel and Rosalind</b> in Millbrook CA</div>
  <p>We want to express our sincere thanks to all of you for all your hard work in making our dream come true.&nbsp; I know a lot of things had to happen behind the scenes and I wanted to thank you for your patience and understanding during this process. ... feel incredibly blessed during this Thanksgiving holiday.</p>
</div>

<div class="abs say-dot"></div>
<h2 class="abs say-title">What we say?</h2>

<section class="abs tweet-band"></section>

<article class="tweet faded" style="left:-34px">
  <div class="tweet-head"><div class="avatar" role="img" aria-label="Profile photo"></div><div><div class="tweet-name">Maren Holt</div><div class="tweet-handle">@marenholt</div></div><span class="follow">Follow</span></div>
  <div class="tweet-text">Lorem ipsum dolor sit amet, consectetur adipiscing elit. Sed aliquam aliquam pretium. Aenean id tortor turpis. Donec pretium ligula <a>eu vehi...</a></div>
  <div class="tweet-time">2:31 AM - 20 Oct 2015</div>
  <div class="tweet-actions"><span>↩</span><span>⇄ 1</span><span>♥ 1</span></div>
</article>

<div class="abs arrow" style="left:400px">‹</div>

<article class="tweet" style="left:434px">
  <div class="tweet-head"><div class="avatar" role="img" aria-label="Profile photo"></div><div><div class="tweet-name">Maren Holt</div><div class="tweet-handle">@marenholt</div></div><span class="follow">Follow</span></div>
  <div class="tweet-text">Lorem ipsum dolor sit amet, consectetur adipiscing elit. Sed aliquam aliquam pretium. Aenean id tortor turpis. Donec pretium ligula <a>eu vehi...</a></div>
  <div class="tweet-time">2:31 AM - 20 Oct 2015</div>
  <div class="tweet-actions"><span>↩</span><span>⇄ 1</span><span>♥ 1</span></div>
</article>

<div class="abs arrow" style="left:826px">›</div>

<article class="tweet faded" style="left:902px">
  <div class="tweet-head"><div class="avatar" role="img" aria-label="Profile photo"></div><div><div class="tweet-name">Maren Holt</div><div class="tweet-handle">@marenholt</div></div><span class="follow">Follow</span></div>
  <div class="tweet-text">Lorem ipsum dolor sit amet, consectetur adipiscing elit. Sed aliquam aliquam pretium. Aenean id tortor turpis. Donec pretium ligula <a>eu vehi...</a></div>
  <div class="tweet-time">2:31 AM - 20 Oct 2015</div>
  <div class="tweet-actions"><span>↩</span><span>⇄ 1</span><span>♥ 1</span></div>
</article>

<footer>
  <div class="abs foot-brand">Fern Wellness &amp; Health</div>
  <div class="abs copyright">© 2013-2015 Fernleaf Studio SL. All rights reserved.</div>
  <div class="abs go-top"><span class="ring"><svg width="12" height="12" viewBox="0 0 12 12"><path d="M6 10V2M2.5 5.5L6 2l3.5 3.5" fill="none" stroke="#f78f20" stroke-width="2"/></svg></span>GO TOP</div>
  <div class="abs foot-team"><span class="mark"></span>Meet our team</div>
  <div class="abs foot-address">14 Alder Lane, Kestrel<br>Vale, KV3 9PN</div>
</footer>

</body>
</html>
```